Tomuvin 30ml pipette jar Mental Health

Label and Box for 30ml amber jar with pipette.
Already have a sample design, that needs to be adapted and possibly improved for the new packaging.
Dark brown letters on White Label.
The jar 30ml with pipette / dropper is amber with dark cap. Please view the photo.
Please view all the files, which I am uploading.
Please provide a mock up version.
Thank you.

Target Market(s)

Upscale women 34-59

Industry/Entity Type

Nutrition, Medical

Requirements
Must have
• Conservative, Minimalistic, Luxury
Should not have
• Leaves

```html
<!DOCTYPE html>
<html lang="en">
<head>
<meta charset="utf-8">
<title>Tomuvin 30ml – Box Dieline and Bottle Label</title>
<link rel="stylesheet" href="https://fonts.googleapis.com/css2?family=Roboto:wght@300;400;500;700&display=swap">
<style>
  :root {
    --stage: #e2e2e2;
    --paper: #ffffff;
    --brand-brown: #6b4226;
    --mark-gold: #c9a36b;
    --ink: #3a3a3a;
    --ink-soft: #6a6a6a;
    --cut-line: #b9b9b9;
    --rule: #8a8a8a;
    --decor: #f3f3f3;
  }
  * { box-sizing: border-box; margin: 0; padding: 0; }
  html, body { width: 1200px; height: 675px; overflow: hidden; }
  body {
    background: var(--stage);
    font-family: "Roboto", sans-serif;
    color: var(--ink);
    position: relative;
  }
  .box-dieline {
    position: absolute;
    left: 70px;
    top: 22px;
    width: 478px;
    height: 627px;
  }
  .box-dieline .cut { fill: var(--paper); stroke: var(--cut-line); stroke-width: 1.4; }
  .box-dieline .fold { stroke: var(--cut-line); stroke-width: 1.2; fill: none; }
  .box-dieline .decor { fill: var(--decor); }
  .box-dieline text { font-family: "Roboto", sans-serif; fill: var(--ink); }
  .box-dieline .product-name { font-weight: 500; fill: var(--brand-brown); font-size: 40px; letter-spacing: 0.5px; }
  .box-dieline .volume { font-weight: 300; font-size: 19px; }
  .box-dieline .category { font-weight: 400; font-size: 15px; }
  .box-dieline .claim-strong { font-weight: 500; font-size: 12.5px; }
  .box-dieline .claim { font-weight: 400; font-size: 12.5px; }
  .box-dieline .fine { font-size: 7.6px; fill: var(--ink-soft); }
  .box-dieline .fine-bold { font-size: 7.6px; font-weight: 700; fill: var(--ink); }
  .box-dieline .facts-title { font-size: 10px; font-weight: 700; }
  .box-dieline .mark-dot { fill: none; stroke: var(--mark-gold); stroke-width: 2; }
  .box-dieline .rule { stroke: var(--rule); stroke-width: 1; }
  .box-dieline .notice-frame { fill: none; stroke: var(--ink); stroke-width: 1.2; }

  .bottle-label {
    position: absolute;
    left: 600px;
    top: 150px;
    width: 560px;
    height: 268px;
    background: var(--paper);
    border: 1px solid var(--cut-line);
  }
  .label-facts {
    position: absolute;
    left: 24px;
    top: 20px;
    width: 188px;
    font-size: 5.6px;
    line-height: 1.35;
    color: var(--ink-soft);
  }
  .label-facts h3 { font-size: 7px; font-weight: 700; color: var(--ink); margin-bottom: 6px; }
  .label-facts .row { display: flex; justify-content: space-between; width: 120px; }
  .label-facts hr { border: 0; border-top: 1px solid var(--rule); margin: 6px 0; }
  .label-facts b { color: var(--ink); }
  .label-facts .gap { height: 5px; }
  .label-notice {
    position: absolute;
    left: 130px;
    top: 220px;
    width: 108px;
    height: 27px;
    border: 1px solid var(--ink);
    font-size: 4.2px;
    line-height: 1.4;
    padding: 3px 4px;
    color: var(--ink-soft);
  }
  .label-signature {
    position: absolute;
    left: 270px;
    top: 150px;
    transform: rotate(-90deg);
    transform-origin: left top;
    font-size: 12px;
    font-weight: 400;
    color: var(--ink);
    white-space: nowrap;
  }
  .label-front {
    position: absolute;
    left: 340px;
    top: 22px;
    width: 170px;
  }
  .category-line { display: flex; align-items: center; gap: 8px; font-size: 14px; font-weight: 400; }
  .category-line .mark-dot {
    width: 20px; height: 20px; border-radius: 50%;
    border: 2px solid var(--mark-gold);
  }
  .label-front .product-name {
    margin-top: 30px;
    font-size: 34px;
    font-weight: 500;
    color: var(--brand-brown);
    letter-spacing: 0.5px;
    line-height: 1;
  }
  .label-front .volume { text-align: right; font-size: 17px; font-weight: 300; margin-top: 6px; padding-right: 0; width: 168px; }
  .label-front .claims { margin-top: 30px; font-size: 11.5px; line-height: 1.35; }
  .label-front .claims strong { font-weight: 500; display: block; }
  .label-decor {
    position: absolute;
    right: 0;
    top: 0;
    width: 40px;
    height: 100%;
    background: linear-gradient(90deg, rgba(243,243,243,0), var(--decor));
  }
</style>
</head>
<body>

<svg class="box-dieline" viewBox="1095 175 880 1150" role="group" aria-label="Folding carton dieline for Tomuvin 30ml">
  <!-- top flaps -->
  <path class="cut" d="M1110 435 L1145 318 L1310 318 L1310 435 Z"/>
  <path class="cut" d="M1310 435 L1310 250 Q1310 185 1370 185 L1450 185 Q1510 185 1510 250 L1510 435 Z"/>
  <line class="fold" x1="1310" y1="250" x2="1510" y2="250"/>
  <path class="cut" d="M1510 435 L1510 318 L1675 318 L1712 435 Z"/>
  <!-- body panels -->
  <rect class="cut" x="1110" y="435" width="802" height="625"/>
  <line class="fold" x1="1310" y1="435" x2="1310" y2="1060"/>
  <line class="fold" x1="1510" y1="435" x2="1510" y2="1060"/>
  <line class="fold" x1="1712" y1="435" x2="1712" y2="1060"/>
  <path class="cut" d="M1912 435 L1960 462 L1960 1030 L1912 1060 Z"/>
  <!-- bottom flaps -->
  <path class="cut" d="M1110 1060 L1310 1060 L1275 1180 L1110 1180 Z"/>
  <path class="cut" d="M1510 1060 L1712 1060 L1712 1180 L1548 1180 Z"/>
  <path class="cut" d="M1712 1060 L1912 1060 L1912 1240 Q1912 1305 1852 1305 L1772 1305 Q1712 1305 1712 1240 Z"/>
  <line class="fold" x1="1712" y1="1240" x2="1912" y2="1240"/>

  <!-- faint decorative motif along the panel bottoms -->
  <g role="img" aria-label="Faint outline decoration">
    <rect class="decor" x="1210" y="810" width="95" height="240" rx="45"/>
    <rect class="decor" x="1318" y="810" width="115" height="240" rx="50"/>
    <rect class="decor" x="1588" y="810" width="115" height="240" rx="50"/>
    <rect class="decor" x="1718" y="810" width="115" height="240" rx="50"/>
  </g>

  <!-- lid (upside down) -->
  <g transform="rotate(180 1410 350)">
    <circle class="mark-dot" cx="1352" cy="306" r="11"/>
    <text class="category" x="1370" y="311">Mental Health</text>
    <text class="product-name" x="1338" y="378">TOMUVIN</text>
    <text class="volume" x="1480" y="407" text-anchor="end">30ml</text>
  </g>

  <!-- front panel A -->
  <circle class="mark-dot" cx="1354" cy="526" r="11"/>
  <text class="category" x="1372" y="532">Mental Health</text>
  <text class="product-name" x="1338" y="607">TOMUVIN</text>
  <text class="volume" x="1482" y="632" text-anchor="end">30ml</text>
  <text class="claim-strong" x="1340" y="724">Doctor Formulated</text>
  <text class="claim" x="1340" y="737">Developed in Clinical Practice</text>

  <!-- front panel B -->
  <circle class="mark-dot" cx="1753" cy="526" r="11"/>
  <text class="category" x="1771" y="532">Mental Health</text>
  <text class="product-name" x="1737" y="607">TOMUVIN</text>
  <text class="volume" x="1881" y="632" text-anchor="end">30ml</text>
  <text class="claim-strong" x="1739" y="724">Doctor Formulated</text>
  <text class="claim" x="1739" y="737">Developed in Clinical Practice</text>

  <!-- facts panel -->
  <text class="facts-title" x="1543" y="597">Product Facts</text>
  <text class="fine" x="1543" y="608">Serving Size:</text>
  <text class="fine" x="1630" y="608">20 drops</text>
  <text class="fine" x="1543" y="620">Servings per Container:</text>
  <text class="fine" x="1630" y="620">30</text>
  <line class="rule" x1="1543" y1="627" x2="1658" y2="627"/>
  <text class="fine-bold" x="1543" y="637">Active Formula: <tspan class="fine">280mg</tspan></text>
  <text class="fine" x="1543" y="646">(% of Daily Value not Established)</text>
  <text class="fine" x="1543" y="653">Pyridoxine, Cobalamin, Folic Acid,</text>
  <text class="fine" x="1543" y="660">Cannabidiol, Aroma Lemon,</text>
  <text class="fine" x="1543" y="667">Aroma Orange, Hemp oil,</text>
  <text class="fine" x="1543" y="674">Lithium Orotate.</text>
  <line class="rule" x1="1543" y1="680" x2="1658" y2="680"/>
  <text class="fine-bold" x="1543" y="693">Directions:</text>
  <text class="fine" x="1543" y="701">Shake well to mix ingredients before use.</text>
  <text class="fine" x="1543" y="709">Take one pipette or more after meals.</text>
  <text class="fine" x="1543" y="716">Adjust daily dose to your needs.</text>
  <text class="fine" x="1543" y="724">Do not exceed four pipettes per day.</text>
  <text class="fine-bold" x="1543" y="732">EU only: <tspan class="fine">Apply content to clean dry skin.</tspan></text>
  <text class="fine" x="1543" y="740">For external use.</text>
  <text class="fine" x="1543" y="748">For best results visit www.calmharborlabs.com</text>
  <line class="rule" x1="1543" y1="752" x2="1658" y2="752"/>
  <text class="fine-bold" x="1543" y="765">Warning:</text>
  <text class="fine" x="1543" y="773">Not to be used by children under 18 years,</text>
  <text class="fine" x="1543" y="781">women who are pregnant or breastfeeding.</text>

  <!-- maker panel -->
  <text class="fine" x="1142" y="900">Manufactured in the EU for</text>
  <text class="fine-bold" x="1142" y="910">Calm Harbor Labs, LLC</text>
  <text class="fine" x="1142" y="920">From Globally Sourced Ingredients</text>
  <text class="fine" x="1142" y="940">Calm Harbor Labs, LLC</text>
  <text class="fine" x="1142" y="950">Fairview, Colorado</text>
  <text class="fine" x="1142" y="960">USA</text>
  <text class="fine" x="1142" y="970">Ph. 555-014-2290</text>
  <text class="fine" x="1142" y="980">www.calmharborlabs.com</text>
  <rect class="notice-frame" x="1141" y="996" width="110" height="34"/>
  <text class="fine" x="1146" y="1007" font-size="5.4">The FDA has not evaluated these statements.</text>
  <text class="fine" x="1146" y="1015" font-size="5.4">This product is not intended to diagnose,</text>
  <text class="fine" x="1146" y="1023" font-size="5.4">treat, cure, or prevent any disease.</text>
</svg>

<section class="bottle-label" aria-label="Bottle label for Tomuvin 30ml">
  <div class="label-facts">
    <h3>Product Facts</h3>
    <div class="row"><span>Serving Size:</span><span>20 drops</span></div>
    <div class="row"><span>Servings per Container:</span><span>30</span></div>
    <hr>
    <p><b>Active Formula:</b> 280mg (% of Daily Value not Established)<br>Pyridoxine, Cobalamin, Folic Acid, Cannabidiol, Aroma Lemon,<br>Aroma Orange, Hemp oil, Lithium Orotate.</p>
    <hr>
    <p><b>Directions:</b> Shake well to mix ingredients before use. Take one pipette or more after meals.<br>Adjust daily dose to your needs.<br>Do not exceed four pipettes per day.<br><b>EU only:</b> Apply content to clean dry skin.<br>For external use.<br>For best results visit www.calmharborlabs.com</p>
    <div class="gap"></div>
    <p><b>Warning:</b> Not to be used by children under 18 years, women who are pregnant or breastfeeding.</p>
    <hr>
    <p>Manufactured in the EU for<br><b>Calm Harbor Labs, LLC</b><br>From Globally Sourced Ingredients</p>
    <div class="gap"></div>
    <p>Calm Harbor Labs, LLC<br>Fairview, Colorado<br>USA<br>Ph. 555-014-2290<br>www.calmharborlabs.com</p>
  </div>
  <div class="label-notice">The FDA has not evaluated these statements. This product is not intended to diagnose, treat, cure, or prevent any disease.</div>
  <div class="label-signature">Calm Harbor.</div>
  <div class="label-front">
    <div class="category-line"><span class="mark-dot"></span><span>Mental Health</span></div>
    <div class="product-name">TOMUVIN</div>
    <div class="volume">30ml</div>
    <div class="claims"><strong>Doctor Formulated</strong>Developed in Clinical Practice</div>
  </div>
  <div class="label-decor" role="img" aria-label="Faint outline decoration at the label edge"></div>
</section>

</body>
</html>
```